Brochure 2 fold and Trifold

We need 2 types of brochure (2 fold and Trifold) design for our Brand "VELOURA BRIGHT" Logo (La douceur de Sorène) is in rose gold color
Target Market(s)
Women ages 17 and up
Industry/Entity Type
Supplement
Font styles to use
Serif
Script
Requirements
Must have
- Rose gold color tone make it look premium, minimalist look

```html
<!DOCTYPE html>
<html lang="en">
<head>
<meta charset="utf-8">
<title>Veloura Bright – Brochures</title>
<link rel="stylesheet" href="https://fonts.googleapis.com/css2?family=PT+Serif:ital,wght@0,400;0,700;1,400&family=Playfair+Display:ital@1&family=Prata&family=Roboto:wght@400&display=swap">
<style>
:root{
  --rose-deep:#b4806f;
  --rose-mid:#c99a8a;
  --rose-text:#b27d6c;
  --rose-light:#f1d9cf;
  --rose-pale:#f8ebe5;
  --rose-band:#e8c8bb;
  --ink:#3a2a25;
  --white:#ffffff;
  --bar-blue:#4a86c5;
  --bar-red:#c9413f;
  --bar-orange:#ef8a2d;
  --axis:#888;
}
*{margin:0;padding:0;box-sizing:border-box}
html,body{width:742px;height:1200px;overflow:hidden;background:var(--white)}
body{position:relative;font-family:"PT Serif",serif;color:var(--ink)}
.set-title{position:absolute;left:0;width:742px;text-align:center;font-family:"Roboto",sans-serif;font-size:17px;letter-spacing:.5px;color:#333}
.sheet{position:absolute;width:390px;height:330px;transform:scale(.92);transform-origin:0 0;overflow:hidden;border:1px solid var(--rose-band)}
.abs{position:absolute}
.bg-rose{background:linear-gradient(135deg,var(--rose-pale) 0%,var(--rose-light) 55%,#e3bcae 100%)}
.band-deep{background:var(--rose-deep);color:var(--white)}
.headline{font-family:"Prata",serif;text-align:center;line-height:1.3;color:var(--white)}
.brand{font-family:"Prata",serif;color:var(--rose-text);text-align:center;white-space:nowrap}
.tagline{font-family:"PT Serif",serif;color:var(--rose-mid);text-align:center}
.photo-capsules{background:linear-gradient(160deg,#d9ecea 0%,#7fb3ad 50%,#3f7c78 100%)}
.photo-botanic{background:radial-gradient(ellipse at 35% 40%,#6aa84a 0%,#a9cf8e 35%,#eef1ec 65%,#ffffff 100%)}
.photo-portrait{background:linear-gradient(100deg,rgba(248,235,229,0) 0%,#f0d8cc 30%,#e8c4b2 60%,#d8ab97 100%)}
.distributor{background:var(--white);border:1px solid var(--rose-mid);font-size:6px;padding:4px 5px;font-weight:700}
.cover-card{background:var(--white)}
.maker{font-family:"Prata",serif;color:var(--rose-text);text-align:center;letter-spacing:1px;white-space:nowrap}
.cover-band{background:var(--rose-band);color:var(--ink);text-align:center;font-family:"PT Serif",serif}
.tab{background:var(--rose-deep);color:var(--white);font-weight:700;font-size:6.3px;line-height:1.25;padding:3px 6px;border-radius:0 12px 12px 0;text-transform:uppercase}
.science{font-size:5.4px;line-height:1.35;text-align:justify}
.science li{margin-bottom:3px;margin-left:9px}
.caption{font-size:5.2px;line-height:1.35;text-align:center}
.benefits-title{font-family:"Playfair Display",serif;font-style:italic;color:var(--rose-text);font-size:11px;line-height:1.1}
.benefits{list-style:none;font-style:italic;font-size:6.6px;line-height:1.3;color:var(--ink)}
.benefits li{padding-left:9px;position:relative}
.benefits li::before{content:"";position:absolute;left:0;top:2.5px;border-left:5px solid var(--rose-deep);border-top:2px solid transparent;border-bottom:2px solid transparent}
svg text{font-family:"PT Serif",serif}
</style>
</head>
<body>

<h2 class="set-title" style="top:212px">FLYER - DOUBLE FOLD</h2>

<!-- Double fold: outside -->
<section class="sheet" style="left:8px;top:240px" aria-label="Double fold outside">
  <div class="abs bg-rose" style="left:0;top:0;width:390px;height:330px"></div>
  <svg class="abs" style="left:0;top:0" width="195" height="130" viewBox="0 0 195 130"><path d="M0 0H195V95Q100 80 0 120Z" fill="var(--rose-deep)"/></svg>
  <p class="abs headline" style="left:0;top:20px;width:195px;font-size:13.5px">One of the first<br>Skin &amp; Sun Protection<br>ALL IN ONE</p>
  <div class="abs photo-capsules" role="img" aria-label="Glass serum dropper with clear supplement capsules" style="left:33px;top:88px;width:84px;height:108px"></div>
  <p class="abs brand" style="left:0;top:207px;width:195px;font-size:17px">VELOURA BRIGHT</p>
  <p class="abs tagline" style="left:0;top:238px;width:195px;font-size:8.5px">Nature's solution to skin whitening</p>
  <div class="abs distributor" style="left:12px;top:257px;width:168px;height:60px">Distributed by:</div>

  <svg class="abs" style="left:210px;top:12px" width="160" height="290" viewBox="0 0 160 290"><path d="M0 290V45Q0 0 80 0Q160 0 160 45V290Z" fill="var(--white)"/><path d="M6 60V47Q6 6 80 6Q154 6 154 47V60" fill="none" stroke="var(--rose-mid)" stroke-width="1"/></svg>
  <p class="abs maker" style="left:210px;top:48px;width:160px;font-size:10px">La douceur de Sorène</p>
  <div class="abs" style="left:218px;top:80px;width:144px;height:1px;background:var(--rose-band)"></div>
  <p class="abs brand" style="left:210px;top:88px;width:160px;font-size:13px;color:var(--ink)">VELOURA BRIGHT</p>
  <div class="abs photo-botanic" role="img" aria-label="Green fern frond with two white tomatoes" style="left:220px;top:118px;width:140px;height:142px"></div>
  <div class="abs cover-band" style="left:216px;top:263px;width:148px;height:30px;font-size:7px;line-height:1.35;padding-top:6px">Skin Whitening &amp; Sun Protection<br>all in one</div>
  <p class="abs tagline" style="left:195px;top:301px;width:195px;font-size:11px;color:var(--rose-text)">Oral supplements</p>
</section>

<!-- Double fold: inside -->
<section class="sheet" style="left:375px;top:240px" aria-label="Double fold inside">
  <div class="abs bg-rose" style="left:0;top:0;width:390px;height:330px"></div>
  <div class="abs photo-portrait" role="img" aria-label="Portrait of a young woman with glowing skin" style="left:200px;top:0;width:190px;height:330px"></div>
  <div class="abs tab" style="left:0;top:8px;width:190px">Skin whitening &amp; sun protection:<br>the scientific answer</div>
  <ol class="abs science" style="left:8px;top:36px;width:180px">
    <li>LumiFlora : An award winning natural supplement using non-GMO tomato species rich in colourless carotenoids, phytoene and phytofluene. This patented combination provides superior whitening, UVA and UVB protection, anti-inflammatory and antioxidant properties.</li>
    <li>Polypodium leucotomos : Naturally extracted from a tropical natural fern found in the Americas, it has been used for centuries by the natives for its superior benefits. Now clinically proven to protect against UV radiation due to its antioxidant, anti-inflammatory and DNA repair abilities.</li>
    <li>L-Cysteine: A potent amino acid that has very high skin-whitening abilities. It prevents the production of pigment cells when the skin is exposed to UV rays and stimulates the production of Glutathione, another strong skin-whitening antioxidant.</li>
  </ol>
  <div class="abs tab" style="left:0;top:167px;width:95px">Clinical studies</div>
  <svg class="abs" style="left:6px;top:183px" width="184" height="112" viewBox="0 0 184 112">
    <rect width="184" height="112" fill="var(--white)"/>
    <text x="92" y="8" font-size="5.5" font-weight="700" text-anchor="middle">Average clinical improvement of skin parameters</text>
    <g stroke="#ddd" stroke-width=".4"><line x1="20" y1="15" x2="178" y2="15"/><line x1="20" y1="35" x2="178" y2="35"/><line x1="20" y1="55" x2="178" y2="55"/><line x1="20" y1="75" x2="178" y2="75"/></g>
    <line x1="20" y1="95" x2="178" y2="95" stroke="var(--axis)" stroke-width=".5"/>
    <g font-size="4" fill="#555" text-anchor="end"><text x="17" y="96">0</text><text x="17" y="76">20</text><text x="17" y="56">40</text><text x="17" y="36">60</text><text x="17" y="16">80</text></g>
    <g fill="var(--bar-blue)"><rect x="30" y="55" width="7" height="40"/><rect x="62" y="46" width="7" height="49"/><rect x="94" y="49" width="7" height="46"/><rect x="126" y="77" width="7" height="18"/><rect x="158" y="75" width="7" height="20"/></g>
    <g fill="var(--bar-red)"><rect x="39" y="41" width="7" height="54"/><rect x="71" y="37" width="7" height="58"/><rect x="103" y="23" width="7" height="72"/><rect x="135" y="57" width="7" height="38"/><rect x="167" y="49" width="7" height="46"/></g>
    <g font-size="3.8" fill="#555" text-anchor="middle"><text x="38" y="102">Dryness</text><text x="70" y="102">Roughness</text><text x="102" y="102">Suppleness</text><text x="134" y="102">Complexion evenness</text><text x="166" y="102">Texture</text></g>
    <text x="92" y="109" font-size="3.6" text-anchor="middle">Figure 1: Graphic representation of the average changes in clinical scoring</text>
  </svg>
  <p class="abs caption" style="left:6px;top:298px;width:184px">Skin improvement results of a clinical study conducted by dermatologists measuring skin quality after 12 weeks use of colourless carotenoids<br>(Global Dermatology 2015: 2(4) Page178-182)</p>

  <p class="abs benefits-title" style="left:207px;top:112px">Benefits of<br>VELOURA BRIGHT</p>
  <ul class="abs benefits" style="left:207px;top:138px;width:110px">
    <li>Skin Whitening</li><li>Collagen Protection</li><li>DNA Repair</li><li>Prevents Against Premature Skin Aging</li><li>Enhanced Antioxidant &amp; Anti-inflammatory effects</li><li>Natural UV Protection</li>
  </ul>
  <svg class="abs" style="left:203px;top:225px" width="90" height="72" viewBox="0 0 90 72">
    <g font-size="7" fill="#333" text-anchor="end"><text x="8" y="70">0</text><text x="8" y="53">2</text><text x="8" y="36">4</text><text x="8" y="19">6</text></g>
    <line x1="12" y1="68" x2="88" y2="68" stroke="var(--axis)" stroke-width=".6"/>
    <rect x="24" y="18" width="15" height="50" fill="var(--bar-blue)"/>
    <rect x="40" y="38" width="15" height="30" fill="var(--bar-orange)"/>
    <path d="M32 15Q38 2 48 10" fill="none" stroke="var(--bar-orange)" stroke-width="2"/>
    <path d="M45 13L51 12L48 7Z" fill="var(--bar-orange)"/>
    <text x="50" y="6" font-size="6">-42, 1%</text><text x="54" y="12" font-size="3.8">P&lt;0.05</text>
  </svg>
  <p class="abs caption" style="left:203px;top:300px;width:180px;text-align:left">Reduction in intensity of melasma with usage of daily oral Polypodium Leucotomos for 12 weeks with sunscreen SPF 45<br>(American Journal of Dermatology 2012: 66(4) Page AB21).</p>
</section>

<h2 class="set-title" style="top:566px">FLYER - TRIPLE FOLD</h2>

<!-- Triple fold: outside -->
<section class="sheet" style="left:8px;top:594px" aria-label="Triple fold outside">
  <div class="abs bg-rose" style="left:0;top:0;width:130px;height:330px"></div>
  <div class="abs band-deep" style="left:0;top:0;width:130px;height:76px"></div>
  <p class="abs headline" style="left:0;top:10px;width:130px;font-size:12.5px;line-height:1.25">One of the<br>first Skin &amp;<br>Sun Protection<br>ALL IN ONE</p>
  <div class="abs photo-capsules" role="img" aria-label="Glass serum dropper with clear supplement capsules" style="left:24px;top:80px;width:66px;height:98px"></div>
  <p class="abs brand" style="left:0;top:190px;width:130px;font-size:12.5px">VELOURA BRIGHT</p>
  <p class="abs tagline" style="left:0;top:216px;width:130px;font-size:6.8px">Nature's solution to skin whitening</p>
  <div class="abs distributor" style="left:5px;top:231px;width:120px;height:86px">Distributed by:</div>

  <div class="abs" style="left:130px;top:0;width:260px;height:330px;background:var(--white)"></div>
  <div class="abs photo-botanic" role="img" aria-label="Large green fern frond with two white tomatoes" style="left:134px;top:30px;width:170px;height:244px"></div>
  <p class="abs maker" style="left:262px;top:44px;width:128px;font-size:10px">La douceur de Sorène</p>
  <p class="abs brand" style="left:262px;top:78px;width:128px;font-size:19px;color:var(--ink);line-height:1.2;white-space:normal">VELOURA<br>BRIGHT</p>
  <div class="abs" style="left:130px;top:277px;width:260px;height:53px;background:linear-gradient(90deg,var(--rose-light),var(--rose-band))"></div>
  <p class="abs" style="left:150px;top:294px;width:90px;font-size:8px;text-align:center">Oral Supplements</p>
  <p class="abs" style="left:268px;top:286px;width:120px;font-size:8px;text-align:center;line-height:1.4">Skin Whitening &amp;<br>Sun Protection all in one</p>
</section>

<!-- Triple fold: inside -->
<section class="sheet" style="left:375px;top:594px" aria-label="Triple fold inside">
  <div class="abs bg-rose" style="left:0;top:0;width:390px;height:330px"></div>
  <div class="abs photo-portrait" role="img" aria-label="Portrait of a young woman with glowing skin" style="left:262px;top:0;width:128px;height:205px"></div>
  <div class="abs tab" style="left:0;top:8px;width:165px">Skin whitening &amp; sun protection:<br>the scientific answer</div>
  <ol class="abs science" style="left:6px;top:36px;width:118px">
    <li>LumiFlora : An award winning natural supplement using non-GMO tomato species rich in colourless carotenoids, phytoene and phytofluene. This patented combination provides superior whitening, UVA and UVB protection, anti-inflammatory and antioxidant properties.</li>
    <li>Polypodium leucotomos : Naturally extracted from a tropical natural fern found in the Americas, it has been used for centuries by the natives for its superior benefits. Now clinically proven to protect against UV radiation due to its antioxidant, anti-inflammatory and DNA repair abilities.</li>
  </ol>
  <ol class="abs science" start="3" style="left:136px;top:36px;width:116px">
    <li>L-Cysteine: A potent amino acid that has very high skin-whitening abilities. It prevents the production of pigment cells when the skin is exposed to UV rays and stimulates the production of Glutathione, another strong skin-whitening antioxidant.</li>
  </ol>
  <svg class="abs" style="left:138px;top:110px" width="90" height="66" viewBox="0 0 90 72">
    <g font-size="7" fill="#333" text-anchor="end"><text x="8" y="70">0</text><text x="8" y="53">2</text><text x="8" y="36">4</text><text x="8" y="19">6</text></g>
    <line x1="12" y1="68" x2="88" y2="68" stroke="var(--axis)" stroke-width=".6"/>
    <rect x="24" y="18" width="15" height="50" fill="var(--bar-blue)"/>
    <rect x="40" y="38" width="15" height="30" fill="var(--bar-orange)"/>
    <path d="M32 15Q38 2 48 10" fill="none" stroke="var(--bar-orange)" stroke-width="2"/>
    <path d="M45 13L51 12L48 7Z" fill="var(--bar-orange)"/>
    <text x="50" y="6" font-size="6">-42, 1%</text><text x="54" y="12" font-size="3.8">P&lt;0.05</text>
  </svg>
  <p class="abs caption" style="left:134px;top:178px;width:122px">Reduction in intensity of melasma with usage of daily oral Polypodium Leucotomos for 12 weeks with sunscreen SPF 45 (American Journal of Dermatology 2012: 66(4) Page AB21).</p>

  <div class="abs tab" style="left:0;top:196px;width:95px">Clinical studies</div>
  <svg class="abs" style="left:6px;top:212px" width="180" height="112" viewBox="0 0 184 112">
    <rect width="184" height="112" fill="var(--white)"/>
    <text x="92" y="8" font-size="5.5" font-weight="700" text-anchor="middle">Average clinical improvement of skin parameters</text>
    <g stroke="#ddd" stroke-width=".4"><line x1="20" y1="15" x2="178" y2="15"/><line x1="20" y1="35" x2="178" y2="35"/><line x1="20" y1="55" x2="178" y2="55"/><line x1="20" y1="75" x2="178" y2="75"/></g>
    <line x1="20" y1="95" x2="178" y2="95" stroke="var(--axis)" stroke-width=".5"/>
    <g font-size="4" fill="#555" text-anchor="end"><text x="17" y="96">0</text><text x="17" y="76">20</text><text x="17" y="56">40</text><text x="17" y="36">60</text><text x="17" y="16">80</text></g>
    <g fill="var(--bar-blue)"><rect x="30" y="55" width="7" height="40"/><rect x="62" y="46" width="7" height="49"/><rect x="94" y="49" width="7" height="46"/><rect x="126" y="77" width="7" height="18"/><rect x="158" y="75" width="7" height="20"/></g>
    <g fill="var(--bar-red)"><rect x="39" y="41" width="7" height="54"/><rect x="71" y="37" width="7" height="58"/><rect x="103" y="23" width="7" height="72"/><rect x="135" y="57" width="7" height="38"/><rect x="167" y="49" width="7" height="46"/></g>
    <g font-size="3.8" fill="#555" text-anchor="middle"><text x="38" y="102">Dryness</text><text x="70" y="102">Roughness</text><text x="102" y="102">Suppleness</text><text x="134" y="102">Complexion evenness</text><text x="166" y="102">Texture</text></g>
    <text x="92" y="109" font-size="3.6" text-anchor="middle">Figure 1: Graphic representation of the average changes in clinical scoring</text>
  </svg>
  <p class="abs caption" style="left:192px;top:262px;width:64px;text-align:left">Skin improvement results of a clinical study conducted by dermatologists measuring skin quality after 12 weeks use of colourless carotenoids (Global Dermatology 2015: 2(4) Page178-182)</p>

  <p class="abs benefits-title" style="left:268px;top:208px">Benefits of<br>VELOURA BRIGHT</p>
  <ul class="abs benefits" style="left:268px;top:234px;width:118px">
    <li>Skin Whitening</li><li>Collagen Protection</li><li>DNA Repair</li><li>Prevents Against Premature Skin Aging</li><li>Enhanced Antioxidant &amp; Anti-inflammatory effects</li><li>Natural UV Protection</li>
  </ul>
</section>

</body>
</html>
```